Exciting adult social quiz app needs awesome modern design

A new and exciting app for couples/sexual partners is in the making. It will be available for Orvane and Quillo devices and allow one partner to invite another partner to the game. The partners will answer questions about their sexual desires and needs and then try to guess what the other one answered.

The app needs a high quality design and you can find some general inspiration in a similar social quiz app called "Pear Trail" which can be found in Gadget Depot and Fetch Market. I like some of the basic layouts of this app.

The design should be classy and have a theme that matches the app subject. This is a sexual get-to-know-each-other-app and not a "porn app". I imagine colors might be black and red (not a requirement) and perhaps have some structures, pictures or backgrounds showing a bit of skin. It's important that the game can be accessed by players in the public space (e.g. in a bus, car etc.) without surroundings thinking it's a sex/porn game - but also important that it's exciting in a kind of sexual way. So try to find a fine line.

As the app is for both genders, the design should accommodate this.

Please see app mockups in the attached PDF.

Initially, please show design proposals for screens 13, 16 and 23.
Please notice that screen 16 doesn't have to be exactly those 2 bars - please make some alternative score comparison graphic in your proposal.

Looking forward to seeing your proposal soon!

Target Market(s)

Couples between 18 and 50

Industry/Entity Type

Adult

Requirements
Must have
• Smooth graphics like the app "Pear Trail"
Nice to have
• Several proposals are appreciated. Perhaps you can show your proposals with different colors and object placements so that I can see some different options.

```html
<!DOCTYPE html>
<html lang="en">
<head>
<meta charset="utf-8">
<title>Time to Match – Question</title>
<link href="https://fonts.googleapis.com/css2?family=Open+Sans:wght@300;400;600;800&display=swap" rel="stylesheet">
<style>
  :root {
    --rose-deep: #c63c5d;
    --rose: #e9526a;
    --rose-light: #f68a88;
    --answer-active: #f0606e;
    --answer-bg: #ffffff;
    --answer-text: #2f2f2f;
    --answer-edge: #d6d3d0;
    --photo-light: #f1efed;
    --photo-mid: #ddd6d1;
    --caption: #9a9694;
    --white: #ffffff;
  }
  * { box-sizing: border-box; margin: 0; padding: 0; }
  html, body {
    width: 703px; height: 1200px; overflow: hidden;
    background: var(--photo-light);
    font-family: "Open Sans", Arial, sans-serif;
  }
  .screen { position: relative; width: 703px; height: 1200px; overflow: hidden; }

  .backdrop {
    position: absolute; inset: 0;
    background:
      radial-gradient(ellipse 260px 420px at 420px 760px, var(--photo-mid), transparent 70%),
      radial-gradient(ellipse 200px 300px at 120px 520px, #e4dfdb, transparent 70%),
      linear-gradient(180deg, #ebe8e5 0%, var(--photo-light) 100%);
  }

  .question-header {
    position: absolute; left: 0; top: 0; width: 703px; height: 385px;
    background: linear-gradient(105deg, var(--rose-deep) 0%, var(--rose) 50%, var(--rose-light) 100%);
    color: var(--white); text-align: center;
  }
  .pointer { position: absolute; left: 0; top: 384px; }

  .status-bar {
    position: absolute; left: 0; top: 0; width: 100%; height: 47px;
    display: flex; align-items: center; justify-content: space-between;
    padding: 0 16px; font-size: 22px; font-weight: 400;
  }
  .status-left, .status-right { display: flex; align-items: center; gap: 8px; width: 220px; }
  .status-right { justify-content: flex-end; }
  .status-time { font-weight: 600; }

  .eyebrow { position: absolute; top: 64px; width: 100%; font-size: 22px; font-weight: 300; }
  .question {
    position: absolute; top: 160px; width: 100%;
    font-size: 51px; line-height: 66px; font-weight: 800; letter-spacing: -0.3px;
  }

  .respondent { position: absolute; left: 251px; top: 506px; width: 200px; text-align: center; }
  .avatar {
    width: 200px; height: 200px; border-radius: 50%;
    border: 5px solid var(--white);
    background: radial-gradient(circle at 50% 55%, #d9a27c 0%, #b57f5c 55%, #5f7a48 100%);
    box-shadow: 0 1px 4px rgba(0,0,0,0.15);
  }
  .respondent-caption { margin-top: 14px; font-size: 14px; color: var(--caption); }

  .answers { position: absolute; left: 123px; top: 821px; width: 463px; list-style: none; }
  .answer {
    height: 47px; margin-bottom: 25px;
    background: var(--answer-bg); color: var(--answer-text);
    border-bottom: 2px solid var(--answer-edge);
    display: flex; align-items: center; justify-content: center;
    font-size: 23px; font-weight: 400;
  }
  .answer:nth-child(3) { margin-bottom: 27px; }
  .answer.is-selected { background: var(--answer-active); color: var(--white); border-bottom-color: #d94e5c; }
</style>
</head>
<body>
<main class="screen">
  <div class="backdrop" role="img" aria-label="Soft blurred photo of an embracing couple in light tones"></div>

  <header class="question-header">
    <div class="status-bar">
      <div class="status-left">
        <svg width="56" height="12" viewBox="0 0 56 12" aria-hidden="true">
          <circle cx="6" cy="6" r="5" fill="#fff"/><circle cx="17" cy="6" r="5" fill="#fff"/><circle cx="28" cy="6" r="5" fill="#fff"/>
          <circle cx="39" cy="6" r="4.3" fill="none" stroke="#fff" stroke-width="1.3"/><circle cx="50" cy="6" r="4.3" fill="none" stroke="#fff" stroke-width="1.3"/>
        </svg>
        <span>VOLT</span>
        <svg width="22" height="16" viewBox="0 0 22 16" aria-hidden="true">
          <path d="M1 5.5a14 14 0 0 1 20 0M4.5 9a9 9 0 0 1 13 0M8 12.3a4 4 0 0 1 6 0" fill="none" stroke="#fff" stroke-width="2.2" stroke-linecap="round"/>
          <circle cx="11" cy="14.5" r="1.5" fill="#fff"/>
        </svg>
      </div>
      <span class="status-time">4:21 PM</span>
      <div class="status-right">
        <svg width="12" height="20" viewBox="0 0 12 20" aria-hidden="true">
          <path d="M1 6l9 8-4.5 4V2L10 6l-9 8" fill="none" stroke="rgba(255,255,255,0.6)" stroke-width="1.6"/>
        </svg>
        <span>100%</span>
        <svg width="42" height="18" viewBox="0 0 42 18" aria-hidden="true">
          <rect x="1" y="1" width="36" height="16" rx="3" fill="none" stroke="#fff" stroke-width="1.5"/>
          <rect x="3.5" y="3.5" width="31" height="11" rx="1.5" fill="#fff"/>
          <rect x="38.5" y="6" width="2.5" height="6" rx="1" fill="#fff"/>
        </svg>
      </div>
    </div>
    <p class="eyebrow">Time to Match!</p>
    <h1 class="question">Would you consider<br>threesome?</h1>
  </header>

  <svg class="pointer" width="703" height="74" viewBox="0 0 703 74" aria-hidden="true">
    <defs>
      <linearGradient id="pointerFill" x1="0" x2="703" y1="0" y2="0" gradientUnits="userSpaceOnUse">
        <stop offset="0" stop-color="#c63c5d"/><stop offset="0.5" stop-color="#e9526a"/><stop offset="1" stop-color="#f68a88"/>
      </linearGradient>
    </defs>
    <polygon points="310,0 399,0 355,73" fill="url(#pointerFill)"/>
  </svg>

  <section class="respondent">
    <div class="avatar" role="img" aria-label="Round profile photo of the partner who answered"></div>
    <p class="respondent-caption">Mira Lindqvist said</p>
  </section>

  <ul class="answers">
    <li class="answer">I don’t think so</li>
    <li class="answer is-selected">I am considering it</li>
    <li class="answer">I’ve always wanted to</li>
    <li class="answer">Hells no!</li>
  </ul>
</main>
</body>
</html>
```